Website for a company offering full serivce charging solutions for electric cars

The company "mero-kant" (english: "mero-edge") offering all-in-one-solutions for charging infrastructure for electric mobility.

There are four products:
1- Wallboxes for single-family homes
2- Solutions for property devloper/-management for property parking space
3- All-in-one-charging solution for municipalities/communities
4- Solutions for tourism/hotels/holiday appartments

The Website structure:
1. Main Page
2.1. Product Page Single Homes
2.2. Product Page Property Management / Parking
2.3. Product Page Municipality
2.4. Product Page Tourism
3. Contact Form / Request for information
4. Imprint / Legal

The Website should be built on Wordpress with a powerful possibility to simply add/modify specific landing pages.

We would like you to implement the website later and also maintain it if possible, but we would be able to do minor modifications by ourselfs (for A/B-Testing)

The website should be clear and simple, easy to understand.
Target group is mainly B2C without deeper knowledge of that topic.

It should suggest, that we will provide a very simple way to get the charging infrastructure done.

We need a contact form, maybe we will use Hubspot later.

Attached you will find a draft of the main page and a landing page (for 2.2) - it is just the content, please ignore the design. We would love to let you create a suitable design.
Also you will find some drafts a bit different for the same story.

I added also a few stock photos, but they don't need to be used! If you have better ideas, you are welcome!

Industry/Entity Type

Charging/Electric mobility

Number of Pages Required

2 page

Font styles to use
Sans Serif

Requirements
Must have
• Based on Wordpress, and the designer should be able to implement it on Wordpress on a later step

```html
<!DOCTYPE html>
<html lang="de">
<head>
<meta charset="utf-8">
<title>mero-kant – Ladeinfrastruktur für Elektromobilität</title>
<link href="https://fonts.googleapis.com/css2?family=Exo+2:wght@500;600;700&family=Poppins:wght@400;500;600&display=swap" rel="stylesheet">
<style>
:root{
  --pink:#e0168f;
  --purple:#7b52c9;
  --dark:#0b0d1f;
  --ink:#1b1b24;
  --text:#3b3b45;
  --grey-bg:#f3f3f3;
  --white:#ffffff;
  --grad:linear-gradient(90deg,var(--pink),var(--purple));
}
*{box-sizing:border-box;margin:0;padding:0}
html,body{width:1200px;height:3465px;overflow:hidden}
body{position:relative;background:var(--white);font-family:'Poppins',sans-serif;color:var(--text)}
.abs{position:absolute}
.btn{position:absolute;display:inline-flex;align-items:center;justify-content:center;height:36px;padding:0 20px;border-radius:18px;background:var(--grad);color:var(--white);font-weight:600;font-size:14px}
.btn.in-flow{position:static;width:134px;margin-top:5px}

/* header */
.brand{position:absolute;left:162px;top:30px;display:flex;align-items:center;gap:12px;font-family:'Exo 2',sans-serif;font-weight:600;font-size:29px;color:var(--ink)}
.brand .dot{width:26px;height:26px;border-radius:50%;background:var(--grad)}
.topbar-mail{position:absolute;left:620px;top:18px;font-size:13px;color:var(--ink);display:flex;gap:8px;align-items:center}
.topbar-phone{position:absolute;left:812px;top:10px;width:225px;height:33px;background:var(--grad);clip-path:polygon(12px 0,100% 0,calc(100% - 12px) 100%,0 100%);color:var(--white);font-size:14px;display:flex;align-items:center;justify-content:center;gap:8px}
.nav{position:absolute;left:455px;top:53px;width:745px;height:38px;background:var(--dark);clip-path:polygon(32px 0,100% 0,100% 100%,0 100%)}
.nav a{position:absolute;top:11px;color:var(--white);font-size:13px;text-decoration:none}
.nav a.active::after{content:"";position:absolute;left:0;right:0;bottom:-8px;height:2px;background:var(--grad)}

/* hero */
.hero{position:absolute;left:0;top:90px;width:1200px;height:577px;background:radial-gradient(circle at 78% 50%,#3452a8 0,#1f2c6a 22%,transparent 45%),linear-gradient(100deg,#141628 0%,#232747 45%,#2b3560 70%,#101326 100%)}
.hero-eyebrow{position:absolute;left:163px;top:120px;font-family:'Exo 2',sans-serif;font-weight:600;font-size:32px;color:var(--white)}
.hero-title{position:absolute;left:163px;top:172px;width:600px;font-family:'Exo 2',sans-serif;font-weight:700;font-size:40px;line-height:50px;color:var(--white)}

/* partner */
.section-title{position:absolute;left:0;width:1200px;text-align:center;font-family:'Exo 2',sans-serif;font-weight:700;font-size:30px;line-height:39px;color:var(--ink)}
.photo{position:absolute;border-radius:50%}
.card{position:absolute;left:560px;top:888px;width:478px;height:382px;background:var(--white);border-radius:8px;box-shadow:0 4px 24px rgba(0,0,0,.12);padding:30px}
.card p{font-size:13.5px;line-height:21.5px;letter-spacing:.2px}
.card .quote{border-left:2px solid var(--purple);padding-left:16px;margin-bottom:16px}

/* offers */
.offers{position:absolute;left:0;top:1356px;width:1200px;height:1711px;background:var(--grey-bg)}
.offer-text{position:absolute}
.offer-h{font-family:'Exo 2',sans-serif;font-weight:500;font-size:25px;line-height:32px;color:var(--ink);margin-bottom:18px}
.list{list-style:none;font-size:13px;line-height:20px;color:var(--text)}
.list li{position:relative;padding-left:30px;margin-bottom:15px}
.list li svg{position:absolute;left:0;top:3px}
.sub{list-style:none;margin-top:6px}
.sub li{padding-left:20px;margin-bottom:5px}
.sub li::before{content:"";position:absolute;left:0;top:9px;width:4px;height:4px;border-radius:50%;background:var(--pink)}

/* contact band */
.contact{position:absolute;left:0;top:3067px;width:1200px;height:136px;background:var(--dark)}
.c-item{position:absolute;top:58px;display:flex;gap:12px;color:var(--white);font-size:14px;line-height:22px}
.c-icon{width:48px;height:40px;background:var(--grad);clip-path:polygon(0 0,100% 0,82% 100%,0 100%);display:flex;align-items:center;justify-content:center;padding-right:6px}

/* footer */
.footer-brand{position:absolute;left:0;top:3245px;width:1200px;display:flex;justify-content:center;align-items:center;gap:12px;font-family:'Exo 2',sans-serif;font-weight:600;font-size:25px;color:var(--ink)}
.footer-brand .dot{width:22px;height:22px;border-radius:50%;background:var(--grad)}
.footer-links{position:absolute;left:0;top:3306px;width:1200px;display:flex;justify-content:center;gap:54px;font-size:13px;color:var(--ink)}
.copy{position:absolute;left:0;top:3347px;width:1200px;text-align:center;font-size:13px;color:var(--ink)}
.social{position:absolute;left:0;top:3386px;width:1200px;display:flex;justify-content:center;gap:16px}
.social span{width:38px;height:38px;border-radius:50%;background:var(--grad)}
.bottom-line{position:absolute;left:0;top:3460px;width:1200px;height:5px;background:var(--grad)}
</style>
</head>
<body>
<svg width="0" height="0" style="position:absolute">
  <defs>
    <linearGradient id="arcGrad" x1="0" y1="0" x2="0" y2="1">
      <stop offset="0" stop-color="#e0168f"/><stop offset="1" stop-color="#7b52c9"/>
    </linearGradient>
    <symbol id="plug" viewBox="0 0 16 14">
      <path d="M1 7h4M6 2h5a4 4 0 0 1 0 10H6zM11 4.5v5M13 7h2" fill="none" stroke="#c02aa8" stroke-width="1.6" stroke-linecap="round"/>
    </symbol>
  </defs>
</svg>

<header>
  <div class="brand"><span class="dot"></span>mero-kant.de</div>
  <div class="topbar-mail">
    <svg width="14" height="11" viewBox="0 0 14 11"><rect width="14" height="11" rx="1" fill="#e0168f"/><path d="M1 1l6 5 6-5" fill="none" stroke="#fff" stroke-width="1.3"/></svg>
    info@mero-kant.de.com
  </div>
  <div class="topbar-phone">
    <svg width="12" height="12" viewBox="0 0 24 24"><path d="M6.6 10.8a15 15 0 0 0 6.6 6.6l2.2-2.2a1 1 0 0 1 1-.25 11.4 11.4 0 0 0 3.6.57 1 1 0 0 1 1 1V20a1 1 0 0 1-1 1A17 17 0 0 1 3 4a1 1 0 0 1 1-1h3.5a1 1 0 0 1 1 1c0 1.250.2 2.450.57 3.57a1 1 0 0 1-.25 1z" fill="#fff"/></svg>
    123 456 7890 (Zollfrei)
  </div>
  <nav class="nav">
    <a class="active" style="left:59px">Lösungen</a>
    <a style="left:160px">Unternehmen</a>
    <a style="left:290px">Dienstleistungen</a>
    <a style="left:437px">Karriere</a>
    <a style="left:530px">Kontakt</a>
  </nav>
</header>

<section class="hero" role="img" aria-label="Foto: Ladestecker an einer Ladesäule vor unscharfen Lichtern">
  <div class="hero-eyebrow">mero-kant</div>
  <h1 class="hero-title">All-in-One-Lösungen für Ladeinfrastruktur für Elektromobilität anzubieten.</h1>
  <span class="btn" style="left:162px;top:350px;width:205px">Kontaktiere uns heute</span>
</section>

<section class="partner">
  <h2 class="section-title" style="top:788px">mero-kant ist Ihr Partner</h2>
  <svg class="abs" style="left:0;top:0" width="1200" height="1400"><path d="M469 885 A214 214 0 1 0 224 1234" fill="none" stroke="url(#arcGrad)" stroke-width="14"/></svg>
  <div class="photo" role="img" aria-label="Foto: Frau mit Smartphone lädt ihr Elektroauto bei Sonnenuntergang" style="left:178px;top:868px;width:400px;height:405px;background:radial-gradient(circle at 35% 30%,#f6c46a,#c9803a 40%,#5b4632 70%,#d9d9dc 100%)"></div>
  <div class="card">
    <p class="quote">wenn das Laden nicht nur einfach, sondern die Umsetzung auch aus einer Hand kommen soll Wir bieten Lösungen sowohl für Privatkunden, Geschäfts- kunden als auch Kommunen an, die schnell, fair und ohne Eigenleistung zu einer smarten Ladelösung für E-Fahrzeuge kommen möchten.</p>
    <p>Von der Beratung, über die Installation, Inbetriebnahme bis zur Abrechnung und Wartung bekommen Sie bei mero-kant alles aus einer Hand. Auf Wunsch vermieten wir auch die Ladetechnik und übernehmen im gewerblichen Bereich die direkte Abrechnung mit dem Nutzer.</p>
    <span class="btn" style="left:30px;top:299px;width:135px">Alle Ansehen</span>
  </div>
</section>

<section class="offers">
  <h2 class="section-title" style="top:128px">Fragen Sie Uns Nach Der Auf Ihre Individuellen<br>Bedürfnisse Zugeschnittenen Lösung</h2>

  <div class="offer-text" style="left:163px;top:248px;width:410px">
    <h3 class="offer-h">Als Privatkunde</h3>
    <ul class="list">
      <li><svg width="16" height="14"><use href="#plug"/></svg>Bestandsanalyse mit umfangreicher Beratung über die Möglichkeiten der Umsetzung</li>
      <li><svg width="16" height="14"><use href="#plug"/></svg>Prüfung und Übernahme der Anmeldung verfügbarer Fördermöglichkeiten</li>
      <li><svg width="16" height="14"><use href="#plug"/></svg>Auswahl an smarten Wallbox Lösungen, passend für Ihr Fahrzeug und Ihre Bedürfnisse</li>
      <li><svg width="16" height="14"><use href="#plug"/></svg>Installation inkl. aller notwendigen Materialien und Tätigkeiten (Durchbrüche, Erdarbeiten, etc.)</li>
      <li><svg width="16" height="14"><use href="#plug"/></svg>Inbetriebnahme und Einweisung in die Ladetechnik</li>
      <li><svg width="16" height="14"><use href="#plug"/></svg>Jährlich technische Wartung nach DGUV3</li>
    </ul>
    <span class="btn in-flow">Alle Ansehen</span>
  </div>
  <svg class="abs" style="left:0;top:0" width="1200" height="1711"><path d="M726 271 A214 214 0 1 1 906 657" fill="none" stroke="url(#arcGrad)" stroke-width="14"/></svg>
  <div class="photo" role="img" aria-label="Foto: moderne Reihenhäuser mit Einfahrt" style="left:622px;top:256px;width:400px;height:400px;background:linear-gradient(180deg,#cfdbe8 0%,#e6e1d7 35%,#c9bfae 65%,#7d8a5c 100%)"></div>

  <svg class="abs" style="left:0;top:0" width="1200" height="1711"><path d="M484 754 A214 214 0 1 0 239 1103" fill="none" stroke="url(#arcGrad)" stroke-width="14"/></svg>
  <div class="photo" role="img" aria-label="Foto: Team arbeitet an Laptops an einem Besprechungstisch, Draufsicht" style="left:190px;top:738px;width:400px;height:405px;background:radial-gradient(circle at 50% 50%,#e9e3d9,#cfc5b5 55%,#a89a86 100%)"></div>
  <div class="offer-text" style="left:647px;top:740px;width:410px">
    <h3 class="offer-h">Als Geschäftskunde</h3>
    <ul class="list">
      <li><svg width="16" height="14"><use href="#plug"/></svg>Durchführung einer individuellen Bedarfsanalyse inkl. Ermittlung der Anforderungen für:
        <ul class="sub">
          <li>Haus- und Immobilienverwaltungen</li>
          <li>Dienstleistungs- und Handelsunternehmen</li>
          <li>Hotel und Beherbergungsbetriebe</li>
          <li>Parkraum- und Parkhausbetreiber</li>
          <li>Tourismus, Sport- und Freizeiteinrichtungen</li>
        </ul>
      </li>
      <li><svg width="16" height="14"><use href="#plug"/></svg>Planung und Projektierung des Installationsaufwands inkl. Materialverbrauch</li>
      <li><svg width="16" height="14"><use href="#plug"/></svg>Leasing oder Kauf der Hardware</li>
      <li><svg width="16" height="14"><use href="#plug"/></svg>Normgerechte Installation der Ladeinfrastruktur inkl. Durchbruch-, Brandschutz- und Erdarbeiten</li>
    </ul>
    <span class="btn in-flow">Alle Ansehen</span>
  </div>

  <div class="offer-text" style="left:163px;top:1220px;width:450px">
    <h3 class="offer-h">Als Kommune</h3>
    <ul class="list">
      <li><svg width="16" height="14"><use href="#plug"/></svg>Konzeptionierung möglicher Ladeinfrastrukturen innerhalb Ihrer Gemeinde</li>
      <li><svg width="16" height="14"><use href="#plug"/></svg>Planung und Projektsteuerung inkl. sämtlicher behördlicher Genehmigungsverfahren und Beantragung von Fördermitteln</li>
      <li><svg width="16" height="14"><use href="#plug"/></svg>Fachgerechte Installation und Inbetriebnahme</li>
      <li><svg width="16" height="14"><use href="#plug"/></svg>Regelmäßige Wartung gemäß Vorschrif</li>
      <li><svg width="16" height="14"><use href="#plug"/></svg>Reparatur und Kundenservice</li>
      <li><svg width="16" height="14"><use href="#plug"/></svg>Direkte Abrechnung mit dem Nutzer</li>
      <li><svg width="16" height="14"><use href="#plug"/></svg>Beteiligung der Gemeinde am Umsatz</li>
    </ul>
    <span class="btn in-flow">Alle Ansehen</span>
  </div>
  <svg class="abs" style="left:0;top:0" width="1200" height="1711"><path d="M721 1314 A214 214 0 1 1 901 1700" fill="none" stroke="url(#arcGrad)" stroke-width="14"/></svg>
  <div class="photo" role="img" aria-label="Foto: historisches Thermalbad-Gebäude unter blauem Himmel" style="left:619px;top:1299px;width:400px;height:400px;background:linear-gradient(180deg,#5b9ae0 0%,#9cc2ec 30%,#c9b79a 55%,#8a7660 80%,#b8b2a8 100%)"></div>
</section>

<section class="contact">
  <div class="c-item" style="left:162px">
    <span class="c-icon"><svg width="16" height="16" viewBox="0 0 24 24"><path d="M6.6 10.8a15 15 0 0 0 6.6 6.6l2.2-2.2a1 1 0 0 1 1-.25 11.4 11.4 0 0 0 3.6.57 1 1 0 0 1 1 1V20a1 1 0 0 1-1 1A17 17 0 0 1 3 4a1 1 0 0 1 1-1h3.5a1 1 0 0 1 1 1c0 1.25.2 2.45.57 3.57a1 1 0 0 1-.25 1z" fill="#fff"/></svg></span>
    <div>Anruf<br>123 456 7890 (Zollfrei)</div>
  </div>
  <div class="c-item" style="left:437px">
    <span class="c-icon"><svg width="15" height="12" viewBox="0 0 14 11"><rect width="14" height="11" rx="1" fill="#fff"/><path d="M1 1l6 5 6-5" fill="none" stroke="#b12fb0" stroke-width="1.3"/></svg></span>
    <div>Email<br>info@mero-kant.de.com</div>
  </div>
  <div class="c-item" style="left:710px">
    <span class="c-icon"><svg width="16" height="16" viewBox="0 0 24 24"><path d="M6.6 10.8a15 15 0 0 0 6.6 6.6l2.2-2.2a1 1 0 0 1 1-.25 11.4 11.4 0 0 0 3.6.57 1 1 0 0 1 1 1V20a1 1 0 0 1-1 1A17 17 0 0 1 3 4a1 1 0 0 1 1-1h3.5a1 1 0 0 1 1 1c0 1.25.2 2.45.57 3.57a1 1 0 0 1-.25 1z" fill="#fff"/></svg></span>
    <div>Ein Kleid<br>12 Gebäude, Straße, Stadt, Bundesland</div>
  </div>
</section>

<footer>
  <div class="footer-brand"><span class="dot"></span>mero-kant.de</div>
  <div class="footer-links"><span>AGB</span><span>Datenschutzerklärung</span><span>Impressum</span><span>Kontakt</span><span>Karriere</span><span>FAQs</span></div>
  <p class="copy">Urheberrecht © 2022 mero-kant.de. Alle Rechte vorbehalten.</p>
  <div class="social"><span></span><span></span><span></span></div>
  <div class="bottom-line"></div>
</footer>
</body>
</html>
```